Business card for start up company

SIMPLE, CLEAN, FRESH, MODERN, SOPHISTICATED. professional. experienced, easy to deal with, expert in the field. local ethics.

professional business card for Forge Ahead Works. using company logo supplied and images.

GENERAL ENGINEERING - MACHINING - WELDING - MAINTENANCE

Forge Ahead Works Ltd is a locally owned mechanical engineering company that specialises in general and mechanical engineering, as well as steel fabrication, welding, repairs and maintenance.

We specialise in the design, welding, fabrication and installation of stainless and mild steel fabrications. We service commercial and residential clients; large or small projects; production line or one off designs.

We have built a solid reputation for quality and service for our machinery and engineering work around Northland NZ. For innovative, cost effective and efficient engineering solutions, to suit a wide range of commercial, residential and rural applications.

Target Market(s)

boat builders. DIY. industrial. RESIDENTIAL. COMMERCIAL

Industry/Entity Type

Mechanical Engineering

Contact Information for Business Card

CONTACT / SERVICES SIDE
Forge Ahead Works Ltd.
Design | Machining | Welding | Fabrication | Installation | Maintenance
www.forgeaheadworks.example.nz
grant@forgeaheadworks.example.nz

Font styles to use
Serif

Colors

Designer to choose colors to be used in the design.

Requirements
Must have
• LOGO ONLY WITH NEGATIVE SPACE ON FRONT SIDE
• services and contact side , either use stock photos (supplied) as background or background supplied in logo photos.
Nice to have
• use the symbol icon in logo on contact/ services side, , enlarged, transparent and faded into the background with text over the top on the
• Design | Machining | Welding | Fabrication | Installation | Maintenance
• the above services to be subtle, along the bottom edge of the services side. can i also have another proof with eh above services featuring on the bottom edge of the LOGO FRONT side to see if the text looks better with or without.
Should not have
• crowded, busy, different fonts. different casing.
• use fonts in the logo files designer to make font decision.

```html
<!DOCTYPE html>
<html lang="en">
<head>
<meta charset="utf-8">
<title>Forge Ahead Works – Business Card</title>
<link href="https://fonts.googleapis.com/css2?family=Roboto:wght@300;400;500;700&display=swap" rel="stylesheet">
<style>
  :root {
    --page-bg: #e3e4e6;
    --card-dark: #0d0d0e;
    --card-mid: #2b2b2d;
    --card-light: #47474a;
    --text-light: #f2f2f2;
    --text-logo: #d9d9da;
    --accent: #e4572e;
  }
  * { margin: 0; padding: 0; box-sizing: border-box; }
  html, body {
    width: 1200px; height: 1200px; overflow: hidden;
    background: var(--page-bg);
    font-family: "Roboto", Arial, sans-serif;
  }
  .card {
    position: absolute; left: 180px;
    width: 840px; height: 475px;
    overflow: hidden;
    box-shadow: 4px 6px 10px rgba(0,0,0,0.35);
  }
  .card--front { top: 62px; }
  .card--back { top: 633px; }
  .card__photo { position: absolute; inset: 0; }
  .card--front .card__photo {
    background:
      radial-gradient(ellipse 45% 55% at 62% 35%, #3a3a3c 0%, rgba(30,30,32,0) 70%),
      linear-gradient(170deg, var(--card-dark) 0%, var(--card-mid) 55%, var(--card-light) 100%);
  }
  .card--back .card__photo {
    background:
      linear-gradient(155deg, var(--card-dark) 0%, #1a1a1b 40%, #3b3b3d 62%, #1c1c1d 78%, var(--card-dark) 100%);
  }
  .brand {
    position: absolute; display: flex; flex-direction: column; align-items: center;
  }
  .brand__square {
    width: 14px; height: 14px; background: var(--accent); margin-bottom: 18px;
  }
  .brand__name {
    font-weight: 500; color: var(--text-logo);
    text-transform: uppercase; text-align: center; line-height: 1.05;
  }
  .card--front .brand { left: 0; right: 0; top: 150px; }
  .card--front .brand__name { font-size: 50px; letter-spacing: 1px; }
  .card--back .brand { left: 70px; width: 280px; top: 205px; }
  .card--back .brand__name { font-size: 40px; }
  .services {
    position: absolute; left: 0; right: 0; text-align: center;
    color: var(--text-light); font-weight: 300; font-size: 22px; white-space: nowrap;
  }
  .card--front .services { top: 360px; }
  .card--back .services { top: 55px; }
  .contact { position: absolute; left: 435px; top: 218px; color: var(--text-light); }
  .contact__company { font-weight: 700; font-size: 28px; color: #e6e6e6; margin-bottom: 22px; }
  .contact__line { display: flex; align-items: center; font-size: 22px; font-weight: 300; margin-bottom: 12px; }
  .contact__icon { width: 24px; height: 24px; margin-right: 16px; flex: none; }
</style>
</head>
<body>
  <section class="card card--front">
    <div class="card__photo" role="img" aria-label="Dark close-up photograph of machined steel gears and threaded parts"></div>
    <div class="brand">
      <span class="brand__square"></span>
      <span class="brand__name">Forge Ahead<br>Works</span>
    </div>
    <p class="services">Design | Machining | Welding | Fabrication | Installation | Maintenance</p>
  </section>

  <section class="card card--back">
    <div class="card__photo" role="img" aria-label="Dark close-up photograph of a threaded steel shaft and gear teeth"></div>
    <p class="services">Design | Machining | Welding | Fabrication | Installation | Maintenance</p>
    <div class="brand">
      <span class="brand__square"></span>
      <span class="brand__name">Forge Ahead<br>Works</span>
    </div>
    <div class="contact">
      <p class="contact__company">Forge Ahead Works Ltd.</p>
      <p class="contact__line">
        <svg class="contact__icon" viewBox="0 0 24 24" aria-hidden="true">
          <circle cx="12" cy="12" r="4" fill="none" stroke="#e4572e" stroke-width="2"/>
          <path d="M16 8v5.5a2.5 2.5 0 0 0 5 0V12a9 9 0 1 0-3.5 7.1" fill="none" stroke="#e4572e" stroke-width="2" stroke-linecap="round"/>
        </svg>
        grant@forgeaheadworks.example.nz
      </p>
      <p class="contact__line">
        <svg class="contact__icon" viewBox="0 0 24 24" aria-hidden="true">
          <g fill="none" stroke="#e4572e" stroke-width="1.6">
            <circle cx="12" cy="12" r="10"/>
            <ellipse cx="12" cy="12" rx="4.5" ry="10"/>
            <path d="M2 12h20M4 6.5h16M4 17.5h16"/>
          </g>
        </svg>
        www.forgeaheadworks.example.nz
      </p>
    </div>
  </section>
</body>
</html>
```